Water Filter Company Needs Bizz Cards!!

Need business cards for my company. We sell whole home water filters and salt free water softeners. No more buying bottled water. Our filtering units filter out all heavy metals, chlorine, and VOC's, last 15 years, and are maintenance free and supply your whole home with spring quality alkaline water. Our Salt free water conditioners, eliminate hard water and scale, without lowering the ph, or TDS's (total Dissolved solids)

I think this is the color code we are using on my site. My logo looks good behind it. #192841

Website will be www.Brovexa.com

Industry/Entity Type

Water Purification

Contact Information for Business Card

For now, just insert standard Dummy text. I need these text lines for the info to be editable so i can make them for multiple employees. I do have Photoshop and illustrator, unless there is a simpler program i can use solely for biz cards

Font styles to use
Sans Serif

Requirements
Must have
• Use my preexisting logo.

www.BroVexa.com

Spring Quality Alkaline Water at every tap.

List out services. Whole Home Water Filters, Salt Free Water Softeners, Clarimont KT7, UV Sterilizers
Nice to have
• I think this is the color code we are using on my site. My logo looks good behind it. #192841 or black. Please no white or light blue backgrounds.

Maybe a picture of my tank.

Slogan like Spring Quality Alkaline Water at every tap.
And just list the services Whole Home Water Filters, Salt Free Water Softeners, Clarimont KT7, UV Sterilizers

I think I would like to not have a contrasting textured logo like I see on some of them. I may use it for my personal cards, but new employees may not want the extra expense.
Should not have
• A different logo than the one provided.

White or baby blue backgrounds. Use the color code, or blacks.

```html
<!DOCTYPE html>
<html lang="en">
<head>
<meta charset="utf-8">
<title>Brovexa Business Cards</title>
<link rel="stylesheet" href="https://fonts.googleapis.com/css2?family=Montserrat:wght@400;500;600;700&family=Lora:ital,wght@1,500&display=swap">
<style>
  :root{
    --bg:#2b2c2e;
    --card:#192841;
    --blue:#0a8fd6;
    --sky:#3fb9ec;
    --grey:#bcbdc0;
    --text:#c9d3df;
    --name:#ffffff;
    --rule:#3a4d6c;
  }
  *{margin:0;padding:0;box-sizing:border-box}
  html,body{width:1200px;height:900px;overflow:hidden;background:var(--bg)}
  body{position:relative;font-family:"Montserrat",sans-serif}
  .card{position:absolute;left:250px;width:700px;height:400px;background:var(--card);overflow:hidden;box-shadow:0 10px 30px rgba(0,0,0,.45)}
  .card--front{top:35px}
  .card--back{top:465px}
  .swoosh{position:absolute;left:0;top:0;width:700px;height:400px}
  .tagline{font-family:"Lora",serif;font-style:italic;font-weight:500;font-size:19px;fill:#fff}
  .brand{position:absolute;display:flex;align-items:center;gap:14px;color:var(--sky);font-weight:700;letter-spacing:-1px}
  .brand__dot{border-radius:50%;background:var(--sky)}
  .card--front .brand{left:40px;top:100px;font-size:56px}
  .card--front .brand__dot{width:30px;height:30px}
  .divider{position:absolute;left:345px;top:55px;width:1px;height:170px;background:var(--rule)}
  .contact{position:absolute;left:375px;top:55px;color:var(--text)}
  .contact__name{font-size:26px;font-weight:700;color:var(--name)}
  .contact__name span{color:var(--sky)}
  .contact__role{font-size:14px;font-weight:600;color:var(--sky);margin-bottom:10px}
  .contact__line{font-size:13px;line-height:19px;display:flex;align-items:center;gap:8px}
  .contact__address{margin-bottom:6px}
  .icon{width:12px;height:12px;flex:none}
  .card--back .brand{left:40px;top:55px;font-size:60px}
  .card--back .brand__dot{width:32px;height:32px}
  .services{position:absolute;left:45px;top:150px;list-style:none;color:var(--sky);font-weight:600;font-size:19px}
  .services li{display:flex;align-items:center;gap:10px;line-height:30px}
  .services .icon{width:13px;height:16px}
  .product-photo{position:absolute;left:420px;top:40px;width:250px;height:180px;border-radius:6px;background:linear-gradient(90deg,#0f1012 0 30%,#e6e8d2 30% 62%,#dfe3e8 62% 100%);opacity:.9}
</style>
</head>
<body>

<section class="card card--front">
  <svg class="swoosh" viewBox="0 0 700 400" aria-hidden="true">
    <path fill="var(--grey)" d="M0,360 C260,300 480,300 700,215 L700,232 C480,318 270,318 0,376Z"/>
    <path fill="var(--sky)" d="M40,400 C290,320 500,325 700,245 L700,262 C500,340 310,340 80,400Z"/>
    <path fill="var(--blue)" d="M110,400 C330,335 520,345 700,280 L700,400Z"/>
    <path id="front-curve" fill="none" d="M330,390 C450,365 570,350 700,310"/>
    <text class="tagline"><textPath href="#front-curve">Spring Quality Alkaline Water at every tap</textPath></text>
  </svg>

  <div class="brand"><span class="brand__dot"></span>Brovexa</div>
  <div class="divider"></div>

  <div class="contact">
    <div class="contact__name">Dana <span>Mercer</span></div>
    <div class="contact__role">Director</div>
    <div class="contact__address">
      <div class="contact__line">2480 Harbor Lane</div>
      <div class="contact__line">Portland OR, USA</div>
    </div>
    <div class="contact__line">
      <svg class="icon" viewBox="0 0 12 12"><path fill="var(--sky)" d="M2.5 1 L4.5 1 L5 4 L3.8 5 C4.5 6.5 5.5 7.5 7 8.2 L8 7 L11 7.5 L11 9.5 C11 10.5 10 11 9 11 C4.5 10.5 1.5 7.5 1 3 C1 2 1.5 1 2.5 1Z"/></svg>
      0123 555 014
    </div>
    <div class="contact__line">
      <svg class="icon" viewBox="0 0 12 12"><rect x="1" y="2.5" width="10" height="7" rx="1" fill="var(--sky)"/><path d="M1.5 3 L6 6.5 L10.5 3" stroke="#192841" fill="none"/></svg>
      hello@brovexa.com
    </div>
    <div class="contact__line">
      <svg class="icon" viewBox="0 0 12 12"><circle cx="6" cy="6" r="5" fill="none" stroke="var(--sky)" stroke-width="1.2"/><path d="M1 6 H11 M6 1 C3.5 3.5 3.5 8.5 6 11 M6 1 C8.5 3.5 8.5 8.5 6 11" fill="none" stroke="var(--sky)"/></svg>
      www.Brovexa.com
    </div>
  </div>
</section>

<section class="card card--back">
  <svg class="swoosh" viewBox="0 0 700 400" aria-hidden="true">
    <path fill="var(--grey)" d="M0,340 C260,290 480,300 700,235 L700,252 C480,317 270,307 0,356Z"/>
    <path fill="var(--sky)" d="M0,365 C270,315 490,325 700,265 L700,282 C490,342 280,332 0,382Z"/>
    <path fill="var(--blue)" d="M0,395 C280,345 500,355 700,300 L700,400 L0,400Z"/>
    <path id="back-curve" fill="none" d="M260,392 C400,370 550,360 700,330"/>
    <text class="tagline"><textPath href="#back-curve">Spring Quality Alkaline Water at every tap</textPath></text>
  </svg>

  <div class="brand"><span class="brand__dot"></span>Brovexa</div>

  <ul class="services">
    <li><svg class="icon" viewBox="0 0 13 16"><path d="M6.5 1 C4 5 2 8 2 10.5 A4.5 4.5 0 0 0 11 10.5 C11 8 9 5 6.5 1Z" fill="none" stroke="var(--sky)" stroke-width="2"/></svg>Whole home water filters</li>
    <li><svg class="icon" viewBox="0 0 13 16"><path d="M6.5 1 C4 5 2 8 2 10.5 A4.5 4.5 0 0 0 11 10.5 C11 8 9 5 6.5 1Z" fill="none" stroke="var(--sky)" stroke-width="2"/></svg>Salt free water softeners</li>
    <li><svg class="icon" viewBox="0 0 13 16"><path d="M6.5 1 C4 5 2 8 2 10.5 A4.5 4.5 0 0 0 11 10.5 C11 8 9 5 6.5 1Z" fill="none" stroke="var(--sky)" stroke-width="2"/></svg>Clarimont KT7</li>
    <li><svg class="icon" viewBox="0 0 13 16"><path d="M6.5 1 C4 5 2 8 2 10.5 A4.5 4.5 0 0 0 11 10.5 C11 8 9 5 6.5 1Z" fill="none" stroke="var(--sky)" stroke-width="2"/></svg>UV Sterilizers</li>
  </ul>

  <div class="product-photo" role="img" aria-label="Product photo: black filter tank, cream softener tank and UV sterilizer unit"></div>
</section>

</body>
</html>
```